DIY Brochure for Velbrook Finishes

Create a brochure for our company and product overview for DIY paint manufacturing business in the UK.

Target Market(s)

DIT paints

Industry/Entity Type

DIY paint and home improvement

Requirements
Must have
• good clear images and text layout

```html
<!DOCTYPE html>
<html lang="en">
<head>
<meta charset="utf-8">
<title>Velbrook Finishes – DIY Paints Brochure</title>
<link href="https://fonts.googleapis.com/css2?family=Montserrat:wght@400;500;600;700;800&display=swap" rel="stylesheet">
<style>
:root{
  --bg:#e9eaec;
  --grey-dark:#555659;
  --grey-mid:#8c8d90;
  --grey-light:#b9babc;
  --blue:#37a6e6;
  --blue-light:#5cc1f2;
  --blue-deep:#1f8fd6;
  --green:#7dc242;
  --ink:#2b2b2b;
  --paper:#f2f2f3;
  --white:#ffffff;
}
*{box-sizing:border-box;margin:0;padding:0}
html,body{width:782px;height:1200px;overflow:hidden}
body{background:var(--bg);font-family:'Montserrat',sans-serif;position:relative;color:var(--ink)}
.spread{position:absolute;box-shadow:0 10px 24px rgba(0,0,0,.25)}
.cover{left:95px;top:76px;width:588px;height:448px}
.inside{left:96px;top:664px;width:590px;height:440px;background:var(--paper)}
.page{position:absolute;top:0;height:100%;overflow:hidden}
.cover .page{width:294px}
.page--left{left:0}
.page--right{right:0}
.page-bg{position:absolute;inset:0}
.intro{position:absolute;left:38px;top:44px;width:214px;color:var(--white)}
.intro-lead{font-size:7.3px;font-weight:500;line-height:1.3;border-left:2px solid var(--green);border-right:2px solid var(--green);padding:0 4px;}
.intro-body{font-size:4.6px;line-height:1.35;margin-top:8px;padding-left:6px;text-align:justify}
.brand{position:absolute;left:0;width:100%;text-align:center;color:var(--white);font-weight:800;letter-spacing:.5px;line-height:.95}
.brand-mark{display:block;width:14px;height:14px;background:var(--green);margin:0 auto 5px}
.brand-name{font-size:19px}
.brand-name small{display:block;font-size:12px}
.contact{position:absolute;left:0;width:100%;text-align:center;color:var(--white);font-weight:500}
.contact-icon{display:block;width:16px;height:18px;margin:0 auto 8px;background:var(--white);border-bottom:2px solid var(--green);border-radius:1px}
.contact-icon svg{display:block;margin:2px auto}
.contact-phone{font-size:11.5px}
.contact-text{font-size:9px}
.tagline{position:absolute;top:174px;width:100%;text-align:center;color:var(--white);font-size:6.6px;font-weight:600}
.product-shot{position:absolute;border-radius:6px;background:linear-gradient(180deg,#f4f5f6 0%,#cfd3d6 70%,#9aa0a4 100%)}
.welcome{position:absolute;left:46px;top:368px;width:206px;height:17px;background:var(--grey-dark);color:var(--white);font-size:11px;font-weight:600;text-align:center;line-height:17px;border-bottom:2px solid var(--green)}
.cover-title{position:absolute;top:398px;width:100%;text-align:center;color:var(--white);font-size:15.5px;font-weight:800}
.inside .page{width:295px;background:var(--paper)}
.band{position:absolute;background:linear-gradient(90deg,var(--blue-light),var(--blue),var(--blue-light));color:var(--white);font-weight:500;text-align:center}
.band--head{left:0;top:0;width:100%;height:28px;font-size:8px;line-height:28px}
.band--section{left:120px;top:183px;width:175px;height:27px;font-size:8px;line-height:27px}
.band--foot{left:0;bottom:0;width:100%;height:30px;font-size:11.5px;line-height:30px}
.band--foot svg{vertical-align:-1px;margin-right:4px}
.item{position:absolute;text-align:center;font-size:6.4px;line-height:1.25;font-weight:500}
.item .shot{width:100%;height:72px;margin-bottom:10px}
.item-name{color:var(--ink)}
.item-spec{color:var(--green)}
.item--side{text-align:left}
.person{position:absolute;background:linear-gradient(180deg,#e6d8cc 0%,#a9b0b6 35%,#2d5cb8 60%,#1f46a0 100%);border-radius:40px 40px 0 0}
</style>
</head>
<body>

<section class="spread cover">
  <div class="page page--left">
    <svg class="page-bg" width="294" height="448" aria-hidden="true">
      <defs>
        <linearGradient id="greyL" x1="0" y1="0" x2="0" y2="1"><stop offset="0" stop-color="#5a5b5e"/><stop offset="1" stop-color="#a7a8ab"/></linearGradient>
        <linearGradient id="blueL" x1="0" y1="0" x2="1" y2="1"><stop offset="0" stop-color="#2f9fe3"/><stop offset=".5" stop-color="#55bdf1"/><stop offset="1" stop-color="#2d9ce2"/></linearGradient>
      </defs>
      <rect width="294" height="448" fill="url(#greyL)"/>
      <polygon points="0,200 144,116 294,200 294,448 0,448" fill="#fff"/>
      <polygon points="0,210 144,126 294,210 294,448 0,448" fill="url(#blueL)"/>
    </svg>
    <div class="intro">
      <p class="intro-lead">We are a second generation, family run, UK based paint manufacturer specialising in functional, premium paints and coatings for DIY and home improvement purposes.</p>
      <p class="intro-body">We take pride that we have been manufacturing paints for over 40 years, and pursue in bringing your vision to life with a diverse palette of high quality, ultra-durable, eco friendly products.</p>
    </div>
    <div class="brand" style="top:188px"><span class="brand-mark"></span><span class="brand-name">VELBROOK<small>FINISHES</small></span></div>
    <div class="contact" style="top:262px">
      <span class="contact-icon"><svg width="12" height="12" viewBox="0 0 12 12"><circle cx="6" cy="6" r="6" fill="#2b2b2b"/><path d="M4 3.2l1.2 1.5-.6.8c.4.8 1 1.4 1.8 1.8l.8-.6 1.5 1.2-.7 1c-2.4-.3-4.4-2.3-4.7-4.7z" fill="#fff"/></svg></span>
      <span class="contact-phone">01632 960418</span>
    </div>
    <div class="contact" style="top:314px">
      <span class="contact-icon"><svg width="12" height="12" viewBox="0 0 12 12"><circle cx="6" cy="6" r="6" fill="#2b2b2b"/><rect x="3" y="4" width="6" height="4.2" fill="#fff"/><path d="M3 4l3 2.4L9 4" stroke="#2b2b2b" stroke-width=".7" fill="none"/></svg></span>
      <span class="contact-text">info@velbrookfinishes.co.uk</span>
    </div>
    <div class="contact" style="top:365px">
      <span class="contact-icon"><svg width="12" height="12" viewBox="0 0 12 12"><circle cx="6" cy="6" r="5" fill="none" stroke="#2b2b2b" stroke-width="1.2"/><ellipse cx="6" cy="6" rx="2" ry="5" fill="none" stroke="#2b2b2b" stroke-width=".8"/><path d="M1 6h10" stroke="#2b2b2b" stroke-width=".8"/></svg></span>
      <span class="contact-text">velbrookfinishes.co.uk</span>
    </div>
  </div>

  <div class="page page--right">
    <svg class="page-bg" width="294" height="448" aria-hidden="true">
      <defs>
        <linearGradient id="greyR" x1="0" y1="0" x2="0" y2="1"><stop offset="0" stop-color="#5a5b5e"/><stop offset="1" stop-color="#a7a8ab"/></linearGradient>
        <linearGradient id="blueR" x1="0" y1="0" x2="1" y2="1"><stop offset="0" stop-color="#2f9fe3"/><stop offset=".5" stop-color="#55bdf1"/><stop offset="1" stop-color="#2d9ce2"/></linearGradient>
      </defs>
      <rect width="294" height="448" fill="url(#greyR)"/>
      <polygon points="0,200 150,116 294,200 294,448 0,448" fill="#fff"/>
      <polygon points="0,210 150,126 294,210 294,448 0,448" fill="url(#blueR)"/>
    </svg>
    <div class="brand" style="top:34px"><span class="brand-mark"></span><span class="brand-name">VELBROOK<small>FINISHES</small></span></div>
    <p class="tagline">Where functionality meets practicality.</p>
    <div class="product-shot" style="left:28px;top:222px;width:244px;height:112px" role="img" aria-label="Group of paint tins: damp seal, direct to rust, anti mould, wood hardener, aqua lacquer and patio paint"></div>
    <div class="welcome">Welcome to Velbrook Finishes</div>
    <p class="cover-title">DIY PAINTS</p>
  </div>
</section>

<section class="spread inside">
  <div class="page page--left">
    <div class="band band--head">Damp Sealing, Anti Mould and Anti Condensation Paints</div>
    <div class="item" style="left:12px;top:42px;width:96px">
      <div class="shot product-shot" style="position:static;margin:0 auto 10px;width:58px" role="img" aria-label="Damp Seal One Coat paint tin"></div>
      <p class="item-name">Damp Seal One Coat</p><p class="item-spec">1, 2.5 &amp; 5 Litres - Matt White</p>
    </div>
    <div class="item" style="left:110px;top:42px;width:80px">
      <div class="shot product-shot" style="position:static;margin:0 auto 10px;width:46px" role="img" aria-label="Anti Mould Paint tin"></div>
      <p class="item-name">Anti Mould Paint</p><p class="item-spec">5 Litre - Matt White</p>
    </div>
    <div class="item" style="left:195px;top:42px;width:90px">
      <div class="shot product-shot" style="position:static;margin:0 auto 10px;width:46px" role="img" aria-label="Anti Condensation Paint tin"></div>
      <p class="item-name">Anti Condensation Paint</p><p class="item-spec">5 Litre - Matt White</p>
    </div>
    <div class="person" style="left:4px;top:150px;width:106px;height:290px" role="img" aria-label="Decorator in blue overalls painting with a roller"></div>
    <div class="band band--section">Leak Prevention &amp; Roofing Paints</div>
    <div class="product-shot" style="left:120px;top:225px;width:58px;height:74px" role="img" aria-label="Rapid Roof Repair paint tin"></div>
    <div class="item item--side" style="left:189px;top:254px">
      <p class="item-name">Rapid Roof Repair</p><p class="item-spec">Grey - 1 Litre<br>Leak Prevention Solution</p>
    </div>
    <div class="product-shot" style="left:122px;top:322px;width:54px;height:72px" role="img" aria-label="Rapid Leak Repair Paint tin"></div>
    <div class="item item--side" style="left:189px;top:343px">
      <p class="item-name">Rapid Leak Repair Paint</p><p class="item-spec">Clear - 2.5 Litre<br>Leak Prevention Solution</p>
    </div>
    <div class="band band--foot" style="left:110px;width:185px"><svg width="11" height="11" viewBox="0 0 12 12"><circle cx="6" cy="6" r="5" fill="none" stroke="#fff" stroke-width="1.2"/><ellipse cx="6" cy="6" rx="2" ry="5" fill="none" stroke="#fff" stroke-width=".8"/><path d="M1 6h10" stroke="#fff" stroke-width=".8"/></svg>velbrookfinishes.co.uk</div>
  </div>

  <div class="page page--right">
    <div class="band band--head">For Gardens (concrete, metal, wood and BBQ &amp; Stoves) Paints</div>
    <div class="item" style="left:10px;top:44px;width:90px">
      <div class="shot product-shot" style="position:static;margin:0 auto 10px;width:48px" role="img" aria-label="Patio Paint tin"></div>
      <p class="item-name">Paint for Patios</p><p class="item-spec">5 Litre - Dark Grey</p>
    </div>
    <div class="item" style="left:104px;top:42px;width:90px">
      <div class="shot product-shot" style="position:static;margin:0 auto 10px;width:46px" role="img" aria-label="BBQ and Stove Paint tin"></div>
      <p class="item-name">BBQ &amp; Stove Paint</p><p class="item-spec">1 Litre - Black Matt</p>
    </div>
    <div class="item" style="left:196px;top:42px;width:90px">
      <div class="shot product-shot" style="position:static;margin:0 auto 10px;width:54px" role="img" aria-label="Direct To Rust paint tin"></div>
      <p class="item-name">Direct To Rust</p><p class="item-spec">1 Litre - Satin</p>
    </div>
    <div class="item" style="left:10px;top:168px;width:90px">
      <div class="shot product-shot" style="position:static;margin:0 auto 10px;width:46px" role="img" aria-label="Masonry Paint tin"></div>
      <p class="item-name">Masonry Paint</p><p class="item-spec">5 Litres - Matt</p>
    </div>
    <div class="item" style="left:100px;top:168px;width:100px">
      <div class="shot product-shot" style="position:static;margin:0 auto 10px;width:56px" role="img" aria-label="Brick and Tile Paint tin"></div>
      <p class="item-name">Brick &amp; Tile Paint</p><p class="item-spec">Brick Red - 1, 2.5 &amp; 5 Litre</p>
    </div>
    <div class="item" style="left:200px;top:168px;width:90px">
      <div class="shot product-shot" style="position:static;margin:0 auto 10px;width:26px" role="img" aria-label="Crystal Clear Lacquer aerosol can"></div>
      <p class="item-name">Crystal Clear Lacquer</p><p class="item-spec">Aerosol | Multi-Surface<br>Protection- Satin 400ml</p>
    </div>
    <div class="product-shot" style="left:30px;top:296px;width:44px;height:100px;background:linear-gradient(180deg,#c7ccd0,#6b4a33 40%,#4a2f1f)" role="img" aria-label="Wood Hardener tin, 500ml"></div>
    <div class="item item--side" style="left:82px;top:344px">
      <p class="item-name">Wood Hardener<br>for Rotted Wood</p><p class="item-spec">Clear Deep Penetrating<br>Wood Hardener<br>Treats All Types of Timber<br>500ml</p>
    </div>
    <div class="band band--foot" style="width:215px"><svg width="11" height="11" viewBox="0 0 12 12"><circle cx="6" cy="6" r="6" fill="#fff"/><path d="M4 3.2l1.2 1.5-.6.8c.4.8 1 1.4 1.8 1.8l.8-.6 1.5 1.2-.7 1c-2.4-.3-4.4-2.3-4.7-4.7z" fill="#37a6e6"/></svg>01632 960418</div>
    <div class="person" style="left:210px;top:300px;width:80px;height:140px" role="img" aria-label="Decorator in blue overalls holding a paint roller"></div>
  </div>
</section>

</body>
</html>
```